PawQuarry Banner contest an ecommerce site for veterinarians

We need banners for our ecommerce site. Our site is a webstore that veterinarians can use to allow their clients to purchase items from them. Each month we have a different theme for our banners. I am looking for banners for January and February and with a refresh coming to our site could be looking at a dozen over the next year. I may potentially choose from multiple designers and increase the payment or will choose one designer for both months .

For January our theme is winter fun. We will be running a contest were people can submit a picture of their pet to our Chatterloop page enjoying the snow or keeping warm. they have a chance to win one of 5 $50 gift certificates to pawquarry. The banner should have a dog and cat and a separate one with just a cat. We will need a French and English banner. We will provide the French translation once the winner has been selected.

For February our theme is dental health. The banner should have a dog and cat and a separate one with just a cat. We will need a French and English banner. We will provide the French translation once the winner has been selected.

Target Market(s)

pet owners

Industry/Entity Type

Veterinary

Colors

Designer to choose colors to be used in the design.

Requirements
Must have
• dimensions for PQ Banner are: 710px x 280px
Nice to have
• I have attached our logo and some screen shoots of our site so you can get a feel of what it look like. you could also go to www.pawquarry.ca and see what the sign in page looks like
Should not have
• images of pet food

```html
<!DOCTYPE html>
<html lang="en">
<head>
<meta charset="utf-8">
<title>PawQuarry Winter Photo Contest Banner</title>
<link rel="stylesheet" href="https://fonts.googleapis.com/css2?family=Bebas+Neue&display=swap">
<style>
  :root {
    --snow-deep: #6f7784;
    --snow-mid: #9aa1ab;
    --snow-light: #d3d6db;
    --tabby-dark: #5a5046;
    --tabby-mid: #8a7d6e;
    --tabby-light: #b9ad9c;
    --ink: #0d0d0d;
    --prize: #ececec;
  }
  html, body {
    margin: 0;
    padding: 0;
    overflow: hidden;
    background: #ffffff;
  }
  .banner {
    position: relative;
    width: 1200px;
    height: 473px;
    overflow: hidden;
    font-family: "Bebas Neue", "Arial Narrow", sans-serif;
  }
  .banner__scene {
    position: absolute;
    inset: 0;
    background:
      radial-gradient(ellipse at 30% 35%, var(--snow-light) 0%, transparent 55%),
      radial-gradient(ellipse at 80% 70%, var(--snow-light) 0%, transparent 45%),
      linear-gradient(135deg, var(--snow-mid) 0%, var(--snow-deep) 55%, var(--snow-mid) 100%);
  }
  .banner__cat {
    position: absolute;
    left: 700px;
    top: 20px;
    width: 520px;
    height: 470px;
    border-radius: 48% 30% 0 40%;
    background:
      radial-gradient(ellipse at 40% 55%, var(--tabby-light) 0%, transparent 50%),
      linear-gradient(160deg, var(--tabby-mid) 0%, var(--tabby-dark) 100%);
  }
  .banner__headline {
    position: absolute;
    left: 40px;
    top: 38px;
    width: 520px;
    margin: 0;
    text-align: center;
    color: var(--ink);
    font-weight: 400;
    font-size: 60px;
    line-height: 82px;
    letter-spacing: 0.06em;
    text-transform: uppercase;
  }
  .banner__line { display: block; }
  .banner__prize {
    display: block;
    color: var(--prize);
    font-size: 96px;
    line-height: 86px;
    letter-spacing: 0.02em;
  }
</style>
</head>
<body>
  <div class="banner">
    <div class="banner__scene" role="img" aria-label="Snowy winter forest with falling snowflakes"></div>
    <div class="banner__cat" role="img" aria-label="Tabby kitten peeking in from the right edge"></div>
    <h1 class="banner__headline">
      <span class="banner__line">Summit a picture</span>
      <span class="banner__line">with your cat</span>
      <span class="banner__line">and win</span>
      <span class="banner__prize">50$</span>
      <span class="banner__line">gift certificate</span>
    </h1>
  </div>
</body>
</html>
```